Walking Food Tour Business In Melbourne.

We need a two sided A4 page flyer
(1) Front Side - Detailing all the 'foodie' venue stops and other spots of interest. We have one already which is attached. What we are looking for is a better design - rather than just words running down the page. Perhaps something in clouds or boxes/circles relatable to food? However important to note, the venues need to change and therefore the 'user' needs to be able to update the page.
(2) Back Side - The back page, we are looking for a CBD map of Melbourne. I have attached one, but open to a more user friendly one if better suited.
Thank you

```html
<!DOCTYPE html>
<html lang="en">
<head>
<meta charset="utf-8">
<title>Foodies Bucket List Tour – Flyer Front and Back</title>
<link href="https://fonts.googleapis.com/css2?family=Lato:wght@400;700&family=Noto+Serif:wght@700&family=Roboto:ital,wght@1,500;1,700&display=swap" rel="stylesheet">
<style>
  :root{
    --board:#484848;
    --ink:#222;
    --blue:#2a7fc4;
    --blue-dark:#1f6aa8;
    --night:#25272a;
    --paper:#fff;
    --label:#f2f2f2;
  }
  *{box-sizing:border-box;margin:0;padding:0}
  html,body{width:1200px;height:1200px;overflow:hidden;background:var(--board)}
  body{position:relative;font-family:"Lato",sans-serif;color:var(--ink)}

  .sheet{position:absolute;top:236px;height:644px;background:var(--paper);box-shadow:0 4px 14px rgba(0,0,0,.45);overflow:hidden}
  .sheet--front{left:114px;width:458px}
  .sheet--back{left:639px;width:461px}
  .sheet svg{position:absolute;left:0;display:block}

  .side-label{position:absolute;top:926px;font-family:"Lato",sans-serif;font-size:29px;letter-spacing:3px;color:var(--label)}
  .side-label--front{left:262px}
  .side-label--back{left:828px}

  .brand{position:absolute;font-family:"Lato",sans-serif;font-weight:700;white-space:nowrap}
  .brand--front{left:322px;top:44px;font-size:15px;color:var(--night)}
  .brand--back{left:0;width:100%;top:72px;text-align:center;font-size:30px;color:var(--paper)}

  .tour-title{position:absolute;left:44px;top:208px;font-family:"Noto Serif",serif;font-weight:700;font-size:28px;color:var(--blue);letter-spacing:.2px;white-space:nowrap}
  .tour-title-rule{position:absolute;left:42px;top:245px;width:354px;height:2px;background:var(--night)}

  .venues{position:absolute;left:10px;top:262px;width:205px}
  .venue{margin-bottom:9px}
  .venue-head{font-size:10.4px;color:var(--blue);line-height:1.25;white-space:nowrap;margin-bottom:2px}
  .venue p{font-size:8.3px;line-height:1.32}
  .venue p.just{text-align:justify}

  .column-rule{position:absolute;left:225px;top:256px;width:1.5px;height:268px;background:var(--night)}
  .spots-rule{position:absolute;left:236px;top:255px;width:2px;height:34px;background:var(--blue)}
  .spots-title{position:absolute;left:241px;top:255px;font-family:"Roboto",sans-serif;font-style:italic;font-weight:700;font-size:13px;line-height:1.25;color:var(--ink)}
  .spots{position:absolute;left:241px;top:291px;width:206px}
  .spot{margin-bottom:3px}
  .spot h3{font-family:"Roboto",sans-serif;font-style:italic;font-weight:500;font-size:10px;color:var(--blue);line-height:1.3}
  .spot p{font-size:7.1px;line-height:1.3}

  .dish{position:absolute;width:72px;height:72px;border-radius:50%;border:3px solid var(--paper);box-shadow:0 0 0 2px var(--blue)}
  .dish--1{left:20px;top:556px;background:radial-gradient(circle at 45% 45%,#e8a33a,#c0621c 60%,#6c8a2e)}
  .dish--2{left:139px;top:556px;background:radial-gradient(circle at 50% 45%,#d9c08a,#c9493a 45%,#f4f1ea 75%)}
  .dish--3{left:245px;top:568px;background:radial-gradient(circle at 45% 40%,#f0cf84,#c88a38 70%)}
  .dish--4{left:365px;top:550px;background:radial-gradient(circle at 50% 50%,#e9e9e4,#7ea060 45%,#111 75%)}

  .web{position:absolute;left:0;width:100%;top:600px;text-align:center;font-family:"Lato",sans-serif;font-weight:700;font-size:10px;letter-spacing:1.3px;color:var(--ink)}
</style>
</head>
<body>

<section class="sheet sheet--front" aria-label="Flyer front">
  <svg width="458" height="260" viewBox="0 0 458 260" style="top:0">
    <defs>
      <linearGradient id="riverPhoto" x1="0" y1="0" x2="0" y2="1">
        <stop offset="0" stop-color="#4d8fd6"/>
        <stop offset=".45" stop-color="#a9b9c9"/>
        <stop offset=".7" stop-color="#6b5e55"/>
        <stop offset="1" stop-color="#3f5a6a"/>
      </linearGradient>
    </defs>
    <path role="img" aria-label="Photo of the city riverbank with trees, a bridge and towers" fill="url(#riverPhoto)" d="M0 0H458V236C400 200 330 172 240 174C140 176 60 205 0 205Z"/>
    <path fill="none" stroke="var(--blue)" stroke-width="3" d="M0 210C60 210 140 181 240 179C330 177 400 205 458 241"/>
  </svg>
  <div class="brand brand--front">Laneway Tastes</div>

  <h1 class="tour-title">Foodies Bucket List Tour</h1>
  <div class="tour-title-rule"></div>

  <div class="venues">
    <div class="venue">
      <div class="venue-head">COCOA LEDGER...... Block Arcade</div>
      <p>Founded in 1915 by Albert Hale from Adelaide<br>Signature Frog</p>
    </div>
    <div class="venue">
      <div class="venue-head">TAPA NORTE...............Hosier Lane</div>
      <p>Tapas Bar &amp; Restaurant with a graffiti art exterior,<br>Signature Anchoa &amp; Croqueta</p>
    </div>
    <div class="venue">
      <div class="venue-head">LOTUS LANE KITCHEN..... Oliver Lane</div>
      <p class="just">Pan Asian street food flavours. An intriguing Asian influences from Shanghai, Hongkong, Seoul and Japan Soft Shell Crab or Eggplant Pancake Roll</p>
    </div>
    <div class="venue">
      <div class="venue-head">INCA GRILL.......................... ACDC Lane</div>
      <p>Peruvian bar and grill<br>Peruano ‘Snapper’ Ceviche, Pastel De Choclo<br>&amp; Alpaca Croquette</p>
    </div>
    <div class="venue">
      <div class="venue-head">CIRRUS &amp; CO.................. Flinders Lane</div>
      <p class="just">Described as a ‘local’ eating - house and bar, rather than a restaurant – this favourite with large industrial New York style windows is located in an old rag trade building.</p>
      <p>Lemon-curd Madeleine &amp; coffee/tea</p>
    </div>
  </div>

  <div class="column-rule"></div>
  <div class="spots-rule"></div>
  <h2 class="spots-title">Some Of Our Favourite Spots<br>On Tour…</h2>
  <div class="spots">
    <div class="spot"><h3>Flinders St Station</h3><p>Completed 1909 this station now enjoys 110,000 commuters and 1500 trains daily</p></div>
    <div class="spot"><h3>Degrave’s Street</h3><p>Originally a ‘service’ lane, now a vibrant and lively laneway</p></div>
    <div class="spot"><h3>Block Arcade</h3><p>Opened in 1892, visit this Italian designed shopping arcade for the Arcadia Tea Rooms, Saffron House Herb &amp; Spice Merchants &amp; Cocoa Ledger Chocolates</p></div>
    <div class="spot"><h3>Royal Arcade</h3><p>Opened in 1870, this spectacular Victorian Arcade is the oldest in Australia.</p></div>
    <div class="spot"><h3>Presgrave Place</h3><p>With kitschy, framed artworks lining the brick walls, and an old - school laneway vibe. Killer brew at 30 ml coffee &amp; cocktails at Corto Bar</p></div>
    <div class="spot"><h3>Hosier Lane</h3><p>Blue stone laneway with some of our cities best street art embraced</p></div>
    <div class="spot"><h3>Duckboard Place</h3><p>Ink Well Bar</p></div>
    <div class="spot"><h3>Malt House Lane</h3><p>Copper Still Bar - Cocktails</p></div>
  </div>

  <svg width="458" height="110" viewBox="0 0 458 110" style="top:534px">
    <path fill="var(--blue)" d="M0 32C100 6 190 14 260 36C330 58 400 40 458 0V110H0Z"/>
    <path fill="var(--night)" d="M0 42C100 18 190 24 260 46C330 68 400 52 458 12V110H0Z"/>
  </svg>
  <div class="dish dish--1" role="img" aria-label="Photo of a vegetable dish"></div>
  <div class="dish dish--2" role="img" aria-label="Photo of a grain salad bowl"></div>
  <div class="dish dish--3" role="img" aria-label="Photo of golden pastries"></div>
  <div class="dish dish--4" role="img" aria-label="Photo of a noodle soup bowl"></div>
</section>

<section class="sheet sheet--back" aria-label="Flyer back">
  <svg width="461" height="648" viewBox="0 0 461 648" style="top:0">
    <defs>
      <linearGradient id="cbdMap" x1="0" y1="0" x2="1" y2="1">
        <stop offset="0" stop-color="#c9cbcd"/>
        <stop offset=".55" stop-color="#b9bcbf"/>
        <stop offset=".8" stop-color="#b8cf6a"/>
        <stop offset="1" stop-color="#6aa0d8"/>
      </linearGradient>
    </defs>
    <path fill="var(--night)" d="M0 0H461V236C380 190 260 160 160 168C90 175 40 190 0 196Z"/>
    <path role="img" aria-label="Street map of the Melbourne CBD with tram routes, parks and the river" fill="url(#cbdMap)" d="M0 196C40 190 90 175 160 168C260 160 380 190 461 236V492C380 530 260 548 180 544C100 540 40 515 0 488Z"/>
    <path fill="none" stroke="var(--blue)" stroke-width="4" d="M0 196C40 190 90 175 160 168C260 160 380 190 461 236"/>
    <path fill="none" stroke="var(--blue)" stroke-width="4" d="M0 488C40 515 100 540 180 544C260 548 380 530 461 492"/>
  </svg>
  <div class="brand brand--back">Laneway Tastes</div>
  <div class="web">www.lanewaytastes.example</div>
</section>

<div class="side-label side-label--front">Front</div>
<div class="side-label side-label--back">Back</div>

</body>
</html>
```